Rig up a website for a Rigging Company

We already have a logo. Looking for a website design that works on plivano.com.
Our rigging company uses semi trucks, forklifts, and similar equipment to move large machines.
Our logo is white, black and red.

Target Market(s)

Medical Industry (moving medical equipment), Utility Industry (power equipment), Food Industry (moving bottling/packing equipment), US Government (large equipment)

Industry/Entity Type

It Company

Coding

Coded - Design and coding required

Number of Pages Required

5+ page

Font styles to use
Sans Serif

Colors
ec1f27
ffffff
0355a3

Requirements
Must have
• Home page, About page, Services Page, and Contact Information page
Nice to have
• Pictures of semi and forklifts and ability to insert our own pictures of our equipment

```html
<!DOCTYPE html>
<html lang="en">
<head>
<meta charset="utf-8">
<title>Harlow Rigging</title>
<link rel="stylesheet" href="https://fonts.googleapis.com/css2?family=Roboto:ital,wght@0,400;0,500;0,700;0,900;1,700;1,900&family=Lato:wght@400;700&display=swap">
<style>
:root{
  --red:#ec1f27;
  --ink:#111111;
  --text:#333333;
  --muted:#555555;
  --white:#ffffff;
  --light:#eeeeee;
  --footer:#050505;
  --line:#dddddd;
  --sky:#5fabd0;
  --beam:#2f4fa8;
  --forklift:#f0c81a;
  --wood:#c49a66;
}
*{box-sizing:border-box;margin:0;padding:0}
html,body{width:1200px;height:2624px;overflow:hidden;background:var(--white)}
body{position:relative;font-family:'Lato',sans-serif;color:var(--text)}
.abs{position:absolute}

/* header */
.site-header{position:absolute;left:0;top:0;width:1200px;height:126px;background:var(--white)}
.brand{left:100px;top:28px;font-family:'Roboto',sans-serif;font-weight:900;font-size:54px;letter-spacing:-1px;color:var(--ink);line-height:1}
.brand small{display:block;font-size:20px;letter-spacing:6px;margin-top:6px;padding-left:4px;font-weight:900;color:var(--red);border-top:2px solid var(--red);border-bottom:2px solid var(--red);line-height:24px;text-align:center}
.topbar{left:684px;top:10px;display:flex;gap:40px;font-size:17px;color:var(--ink);align-items:center}
.topbar span{display:flex;align-items:center;gap:10px}
.topbar .dot{width:36px;height:36px;border-radius:50%;background:var(--red);display:flex;align-items:center;justify-content:center}
.main-nav{top:74px;left:633px;display:flex;font-family:'Roboto',sans-serif;font-size:17px;color:var(--ink)}
.main-nav a{color:inherit;text-decoration:none;padding:0 32px 0 0;margin-right:32px;border-right:1px solid #999;line-height:20px}
.main-nav a:last-child{border:none;margin:0;padding:0}
.main-nav a.active{color:var(--red);position:relative}
.main-nav a.active::after{content:"";position:absolute;left:-2px;top:30px;width:56px;height:3px;background:var(--red)}

/* hero */
.hero{left:0;top:126px;width:1200px;height:539px;background:
  radial-gradient(ellipse 17% 30% at 32% 62%, rgba(240,200,26,.95), rgba(240,200,26,0) 75%),
  radial-gradient(ellipse 9% 30% at 52% 40%, rgba(25,25,25,.75), rgba(25,25,25,0) 80%),
  radial-gradient(ellipse 14% 18% at 63% 36%, rgba(214,172,118,.95), rgba(214,172,118,0) 80%),
  radial-gradient(ellipse 34% 30% at 86% 58%, rgba(180,140,100,.95), rgba(180,140,100,0) 80%),
  radial-gradient(ellipse 22% 22% at 62% 70%, rgba(200,150,100,.9), rgba(200,150,100,0) 80%),
  radial-gradient(ellipse 10% 22% at 92% 20%, rgba(235,232,225,.9), rgba(235,232,225,0) 80%),
  linear-gradient(172deg, rgba(47,79,168,0) 14%, rgba(47,79,168,.8) 18%, rgba(47,79,168,.8) 21%, rgba(47,79,168,0) 26%),
  linear-gradient(180deg,#5aa6cd 0%,#a9d4e6 38%,#8f8a7e 62%,#5f5c57 100%)}
.hero-caption{position:absolute;left:0;bottom:0;width:100%;height:69px;background:rgba(20,20,20,.6);display:flex;align-items:center;justify-content:center;font-family:'Roboto',sans-serif;font-weight:500;font-size:30px;color:var(--white)}
.hero-caption svg{position:absolute;top:22px}

/* section titles */
.section-title{position:absolute;left:0;width:1200px;font-family:'Roboto',sans-serif;font-style:italic;font-weight:900;font-size:31px;color:var(--ink);display:flex;justify-content:center;align-items:center;gap:22px}
.section-title em{color:var(--red);font-style:italic}
.section-title::before,.section-title::after{content:"";width:70px;height:8px;border-top:2px solid var(--red);border-bottom:2px solid var(--red)}
.on-dark{color:var(--white)}

/* serve */
.serve-item{position:absolute;top:795px;width:224px;text-align:center}
.serve-icon{width:119px;height:119px;border-radius:50%;border:2px solid var(--ink);margin:0 auto 28px;display:flex;align-items:center;justify-content:center;background:var(--white)}
.serve-icon .art{background:radial-gradient(circle at 50% 50%,#111 45%,#3a3a3a 80%,rgba(60,60,60,0) 100%)}
.art.medical{width:76px;height:58px;border-radius:40% 40% 30% 30%;background:radial-gradient(ellipse at 50% 50%,#fff 40%,#f7cdd0 80%,rgba(255,255,255,0) 100%)}
.art.utility{width:70px;height:50px;border-radius:10px}
.art.food{width:56px;height:60px;border-radius:8px}
.art.others{width:80px;height:54px;border-radius:18px 18px 6px 6px}
.serve-item.active .serve-icon{background:var(--red);border-color:var(--red);box-shadow:inset 0 0 0 3px var(--red),inset 0 0 0 5px #fff}
.serve-item h3{font-family:'Roboto',sans-serif;font-weight:500;font-size:20px;color:var(--ink);margin-bottom:9px}
.serve-item.active h3{color:var(--red)}
.serve-item p{font-size:13px;line-height:20px;color:var(--muted);padding:0 6px}

/* about */
.about{left:0;top:1083px;width:1200px;height:323px;background:
  radial-gradient(ellipse 30% 40% at 20% 85%, rgba(120,40,40,.45), rgba(120,40,40,0) 80%),
  radial-gradient(ellipse 30% 40% at 80% 85%, rgba(110,50,50,.4), rgba(110,50,50,0) 80%),
  linear-gradient(180deg,#30343a,#1d1e21 60%,#2a2627)}
.about p{position:absolute;left:140px;top:108px;width:920px;text-align:center;font-size:14.5px;line-height:28px;color:#e8e8e8}
.btn{display:inline-block;background:var(--red);color:var(--white);font-family:'Roboto',sans-serif;font-style:italic;font-weight:700;border-radius:3px}
.about .btn{position:absolute;left:545px;top:236px;width:111px;height:33px;line-height:33px;text-align:center;font-size:15px}

/* equipment */
.equipment-grid{left:100px;top:1523px;width:1000px;display:grid;grid-template-columns:repeat(4,246.25px);grid-auto-rows:247px;gap:6px 5px}
.tile{position:relative}
.tile.t1{background:radial-gradient(ellipse 40% 30% at 40% 70%,rgba(70,75,80,.9),rgba(70,75,80,0) 80%),linear-gradient(180deg,#a9b1b8,#707478 60%,#8a8a7e)}
.tile.t2{background:linear-gradient(180deg,#3d3d3d,#6a3a32)}
.tile.t3{background:radial-gradient(ellipse 45% 30% at 45% 72%,rgba(40,35,30,.9),rgba(40,35,30,0) 80%),linear-gradient(180deg,#5f8fc7 0%,#b8bcc0 40%,#8a8a84 75%,#a53a30 100%)}
.tile.t4{background:radial-gradient(ellipse 40% 25% at 50% 65%,rgba(30,110,170,.9),rgba(30,110,170,0) 80%),linear-gradient(180deg,#3f7fd2,#5d95d8 50%,#c8c2b4 100%)}
.tile.t5{background:radial-gradient(ellipse 30% 22% at 68% 60%,rgba(245,245,245,.95),rgba(245,245,245,0) 80%),radial-gradient(ellipse 30% 35% at 25% 70%,rgba(50,100,170,.8),rgba(50,100,170,0) 80%),linear-gradient(180deg,#a4bcd2,#c8d0d4 50%,#7f8a7c)}
.tile.t6{background:radial-gradient(ellipse 40% 25% at 50% 65%,rgba(200,190,170,.8),rgba(200,190,170,0) 80%),linear-gradient(180deg,#a0acb6,#888d8e 55%,#5f615e)}
.tile.t7{background:radial-gradient(ellipse 25% 30% at 55% 45%,rgba(230,230,235,.85),rgba(230,230,235,0) 80%),linear-gradient(180deg,#2c5fb6,#4f7fc8 55%,#4a4f52)}
.tile.t8{background:radial-gradient(ellipse 35% 30% at 35% 68%,rgba(210,40,35,.95),rgba(210,40,35,0) 80%),radial-gradient(ellipse 35% 40% at 80% 45%,rgba(235,238,242,.9),rgba(235,238,242,0) 80%),linear-gradient(180deg,#a8c0da,#d8d4cc 70%,#b0a89c)}
.tile .overlay{position:absolute;inset:0;background:rgba(0,0,0,.62);color:var(--white);text-align:center;padding-top:62px}
.overlay .plus{width:40px;height:40px;border-radius:50%;background:var(--white);margin:0 auto 14px;display:flex;align-items:center;justify-content:center}
.overlay h4{font-family:'Roboto',sans-serif;font-weight:500;font-size:21px;margin-bottom:6px}
.overlay p{font-size:12.5px;line-height:19px;padding:0 12px}

/* clients */
.clients{left:0;top:2073px;width:1200px;height:217px;background:var(--light)}
.client-row{position:absolute;left:100px;top:106px;display:flex;gap:26px}
.client{width:145px;height:69px;background:var(--white);border:1px solid var(--line);display:flex;align-items:center;justify-content:center;gap:8px;font-size:19px;font-weight:700;color:#222}
.client i{width:14px;height:14px;border-radius:50%;background:#222;display:block}
.clients svg{position:absolute;top:98px}

/* footer */
.site-footer{left:0;top:2290px;width:1200px;height:287px;background:var(--footer);color:#ddd}
.f-head{position:absolute;top:40px;font-family:'Roboto',sans-serif;font-weight:500;font-size:14px;color:var(--white);padding-bottom:10px;border-bottom:1px solid #333}
.quick-links{position:absolute;left:100px;top:84px;list-style:none;font-size:12px;line-height:28px}
.quick-links li::before{content:"›";margin:0 10px 0 2px;color:#aaa}
.contact-list{position:absolute;left:266px;top:86px;font-size:13px;line-height:21px}
.contact-list div{position:relative;padding-left:28px;margin-bottom:14px}
.contact-list svg{position:absolute;left:0;top:3px}
.contact-list b{color:var(--white)}
.field{position:absolute;border:1px solid #444;border-radius:3px;background:#0a0a0a;font-size:11px;font-style:italic;color:#888;padding:5px 8px}
.site-footer .btn{position:absolute;left:540px;top:213px;width:126px;height:31px;line-height:31px;text-align:center;font-size:16px;font-style:normal;border-radius:2px}
.f-brand{position:absolute;left:869px;top:68px;width:231px;text-align:center;font-family:'Roboto',sans-serif;font-weight:900;font-size:48px;color:var(--white);line-height:1}
.f-brand small{display:block;font-size:18px;letter-spacing:6px;margin-top:4px;border-top:2px solid #888;border-bottom:2px solid #888;line-height:22px}
.follow{position:absolute;left:869px;top:164px;width:231px;text-align:center;font-family:'Roboto',sans-serif;font-weight:700;font-size:14px;color:var(--white)}
.socials{position:absolute;left:906px;top:192px;display:flex;gap:12px}
.socials span{width:30px;height:30px;border-radius:50%;border:1.5px solid var(--white)}
.copyright{left:0;top:2577px;width:1200px;height:47px;background:var(--red);color:var(--white);font-size:14px;text-align:center;line-height:47px}
</style>
</head>
<body>

<header class="site-header">
  <div class="abs brand">Harlow<small>RIGGING</small></div>
  <div class="abs topbar">
    <span><i class="dot"><svg width="16" height="16" viewBox="0 0 24 24"><path fill="#fff" d="M6.6 10.8a15 15 0 006.6 6.6l2.2-2.2c.3-.3.7-.4 1-.2 1.1.4 2.3.6 3.6.6.6 0 1 .4 1 1V20c0 .6-.4 1-1 1A17 17 0 013 4c0-.6.4-1 1-1h3.5c.6 0 1 .4 1 1 0 1.3.2 2.5.6 3.6.1.3 0 .7-.2 1z"/></svg></i>0145 862 370</span>
    <span><i class="dot"><svg width="16" height="16" viewBox="0 0 24 24"><path fill="#fff" d="M3 5h18v14H3z"/><path d="M3 5l9 7 9-7" stroke="#ec1f27" stroke-width="2" fill="none"/></svg></i>info@harlowrigging.com</span>
  </div>
  <nav class="abs main-nav">
    <a class="active">HOME</a><a>ABOUT</a><a>SERVICES</a><a>CONTACT</a>
  </nav>
</header>

<section class="abs hero" role="img" aria-label="Photo of a yellow forklift lifting large wooden crates beside stacked equipment cases under a blue steel beam">
  <div class="hero-caption">
    <svg style="left:46px" width="16" height="26" viewBox="0 0 16 26"><path d="M13 2L3 13l10 11" stroke="#ddd" stroke-width="2.5" fill="none"/></svg>
    We Have The Equipment and The Experience to Get Your Job Done Right!
    <svg style="right:46px" width="16" height="26" viewBox="0 0 16 26"><path d="M3 2l10 11L3 24" stroke="#ddd" stroke-width="2.5" fill="none"/></svg>
  </div>
</section>

<h2 class="section-title" style="top:708px"><span>WE <em>SERVE</em></span></h2>

<div class="serve-item active" style="left:105px">
  <div class="serve-icon"><div class="art medical" role="img" aria-label="Icon of a medical equipment robot arm"></div></div>
  <h3>MEDICAL BUSINESS</h3>
  <p>Lorem ipsum dolor sit amet, consectetuer adipiscing elit, sed diam nonummy nibh euismod tincidu.</p>
</div>
<div class="serve-item" style="left:360px">
  <div class="serve-icon"><div class="art utility" role="img" aria-label="Icon of a power generator"></div></div>
  <h3>UTILITY BUSINESS</h3>
  <p>Lorem ipsum dolor sit amet, consectetuer adipiscing elit, sed diam nonummy nibh euismod tincidu.</p>
</div>
<div class="serve-item" style="left:614px">
  <div class="serve-icon"><div class="art food" role="img" aria-label="Icon of stacked boxes"></div></div>
  <h3>FOOD BUSINESS</h3>
  <p>Lorem ipsum dolor sit amet, consectetuer adipiscing elit, sed diam nonummy nibh euismod tincidu.</p>
</div>
<div class="serve-item" style="left:870px">
  <div class="serve-icon"><div class="art others" role="img" aria-label="Icon of a crane truck lifting a box"></div></div>
  <h3>OTHERS</h3>
  <p>Lorem ipsum dolor sit amet, consectetuer adipiscing elit, sed diam nonummy nibh euismod tincidu.</p>
</div>

<section class="abs about" role="img" aria-label="Dark-toned photo of mobile cranes and trucks at a job site">
  <h2 class="section-title on-dark" style="top:42px"><span>ABOUT <em>HARLOW RIGGING</em></span></h2>
  <p>Lorem ipsum dolor sit amet, consectetuer adipiscing elit, sed diam nonummy nibh euismod tincidunt ut laoreet dolore magna aliquam erat volutpat. Ut wisi enim ad minim veniam, quis nostrud exerci tation ullamcorper suscipit lobortis nisl ut aliquip ex ea commodo consequat. Duis autem vel eum iriure dolor in hendrerit in vulputate velit esse molestie consequat, vel illum dolore eu feugiat nulla facilisis at vero eros et accumsan et iusto odio dignissim qui blandit praesent luptatum zzril delenit augue duis dolore te feugait nulla facilisi.</p>
  <a class="btn">Read More</a>
</section>

<h2 class="section-title" style="top:1450px"><span>OUR <em>EQUIPMENTS</em></span></h2>

<div class="abs equipment-grid">
  <div class="tile t1" role="img" aria-label="Photo of a crane lifting a transformer"></div>
  <div class="tile t2" role="img" aria-label="Photo of a crane lifting a load">
    <div class="overlay">
      <div class="plus"><svg width="20" height="20" viewBox="0 0 20 20"><path d="M10 2v16M2 10h16" stroke="#222" stroke-width="2"/></svg></div>
      <h4>HENDRERIT ESSE</h4>
      <p>Duis aute irure dolor in reprehenderit<br>voluptate velit esse cillum dolore</p>
    </div>
  </div>
  <div class="tile t3" role="img" aria-label="Photo of a mobile crane beside heavy machinery on a trailer"></div>
  <div class="tile t4" role="img" aria-label="Photo of a crane lifting a wrapped machine"></div>
  <div class="tile t5" role="img" aria-label="Photo of a boom truck lifting a white tank"></div>
  <div class="tile t6" role="img" aria-label="Photo of a crane at an industrial site"></div>
  <div class="tile t7" role="img" aria-label="Photo of a crane hoisting a steel frame"></div>
  <div class="tile t8" role="img" aria-label="Photo of a red forklift carrying a crate"></div>
</div>

<section class="abs clients">
  <h2 class="section-title" style="top:36px"><span>OUR <em>CLIENTS</em></span></h2>
  <svg style="left:56px" width="20" height="48" viewBox="0 0 20 48"><path d="M16 4L4 24l12 20" stroke="#ccc" stroke-width="2" fill="none"/></svg>
  <div class="client-row">
    <div class="client"><i></i>Corvane</div>
    <div class="client">Milbrook</div>
    <div class="client">Tessaly</div>
    <div class="client">Quorra</div>
    <div class="client"><i></i>Corvane</div>
    <div class="client">Veltrix</div>
  </div>
  <svg style="right:56px" width="20" height="48" viewBox="0 0 20 48"><path d="M4 4l12 20L4 44" stroke="#ccc" stroke-width="2" fill="none"/></svg>
</section>

<footer class="abs site-footer">
  <h4 class="f-head" style="left:100px;width:106px">QUICK LINKS</h4>
  <ul class="quick-links"><li>Home</li><li>About</li><li>Services</li><li>Contact</li></ul>

  <h4 class="f-head" style="left:266px;width:215px">CONTACT DETAILS</h4>
  <div class="contact-list">
    <div><svg width="14" height="16" viewBox="0 0 24 24"><path fill="#ec1f27" d="M12 2a7 7 0 00-7 7c0 5 7 13 7 13s7-8 7-13a7 7 0 00-7-7zm0 9.5A2.5 2.5 0 1112 6a2.5 2.5 0 010 5.5z"/></svg><b>Harlow RIGGING</b><br>Lorem Ipsum Dolor Amet<br>Consectetuer Diam-012345</div>
    <div><svg width="14" height="14" viewBox="0 0 24 24"><path fill="#ec1f27" d="M6.6 10.8a15 15 0 006.6 6.6l2.2-2.2c.3-.3.7-.4 1-.2 1.1.4 2.3.6 3.6.6.6 0 1 .4 1 1V20c0 .6-.4 1-1 1A17 17 0 013 4c0-.6.4-1 1-1h3.5c.6 0 1 .4 1 1 0 1.3.2 2.5.6 3.6.1.3 0 .7-.2 1z"/></svg>0145 862 370</div>
    <div><svg width="14" height="12" viewBox="0 0 24 20"><path fill="#ec1f27" d="M1 2h22v16H1z"/><path d="M1 2l11 8 11-8" stroke="#000" stroke-width="2" fill="none"/></svg>info@harlowrigging.com</div>
  </div>

  <h4 class="f-head" style="left:540px;width:266px">QUICK INQUIRY</h4>
  <div class="field" style="left:540px;top:84px;width:132px;height:27px">Name</div>
  <div class="field" style="left:680px;top:84px;width:126px;height:27px">Email</div>
  <div class="field" style="left:540px;top:120px;width:266px;height:28px">Subject</div>
  <div class="field" style="left:540px;top:157px;width:266px;height:49px">Message</div>
  <a class="btn">SUBMIT</a>

  <div class="f-brand">Harlow<small>RIGGING</small></div>
  <div class="follow">FOLLOW US ON:</div>
  <div class="socials"><span></span><span></span><span></span><span></span></div>
</footer>

<div class="abs copyright">Copyright © 2017 Harlow RIGGING. &nbsp;|&nbsp; All Rights Reserved.</div>

</body>
</html>
```